Web design for a relaunch of a technology and knowledge transfer company

Design for the relaunch of an existing website The company specializes in technology and knowledge transfer between companies (and universities). The innovation company (company name) combines many years of experience in technology transfer, innovation management, project management and grant applications. Link: http://www.vorlaufwerkstatt.example The colors of the logo are not very advantageous and can be adjusted a bit. There are currently no picture worlds, these are to be selected by the designer. Abstract motifs are certainly an advantage here (10 motifs). Animated programming could be done (network etc. http://pelvart.qmstudio.example/). In this case a suggestion is made, which we convert programming technically. The structure and contents of the existing pages will be adopted and supplemented. The programming will be done with TYPO3 in responsive form (bootstrap). Required are start page, content page and contact page. -------------------------------------------------- ------------------------------ Web design for a relaunch of a company in technology and knowledge transfer Design for the relaunch of an existing website. The company specializes in technology and knowledge transfer between companies (and universities). The innovation company combines many years of experience in the fields of technology transfer, innovation management, project management and grant application. Link: http://www.vorlaufwerkstatt.example The color of the logo is not exactly advantageous and can be adjusted. There are currently no image worlds, these are to be selected by the designer. Abstract motifs are certainly an advantage here (10 motifs). It could also be made animated programming (network, etc. http://pelvart.qmstudio.example/). In this case, a proposal has to be made, which we implement in terms of programming technology. The structure and contents of the existing pages are taken over and supplemented. Programming is done with TYPO3 in responsive form (bootstrap). Required are homepage, content page and contact page.

```html
<!DOCTYPE html>
<html lang="en">
<head>
<meta charset="utf-8">
<title>Vorlaufwerkstatt</title>
<link href="https://fonts.googleapis.com/css2?family=Open+Sans:ital,wght@0,400;0,600;0,700;1,400&family=Tinos:ital,wght@0,400;1,700&display=swap" rel="stylesheet">
<style>
  :root {
    --ink: #111111;
    --muted: #8a8a8a;
    --accent: #2c2ce0;
    --brand: #3a45a8;
    --band: #ebebeb;
    --card: #ffffff;
    --page: #ffffff;
  }
  * { margin: 0; padding: 0; box-sizing: border-box; }
  html, body { width: 1200px; height: 1200px; overflow: hidden; background: var(--page); }
  body { position: relative; font-family: "Open Sans", sans-serif; color: var(--ink); }

  .site-header { position: absolute; left: 297px; top: 0; width: 686px; height: 42px; }
  .brand { position: absolute; left: 33px; top: 12px; display: flex; align-items: center; gap: 4px; }
  .brand-mark { width: 10px; height: 10px; background: var(--brand); }
  .brand-name { font-size: 8px; font-weight: 600; letter-spacing: .3px; color: var(--brand); text-transform: uppercase; }
  .main-nav { position: absolute; top: 12px; font-size: 13px; color: var(--muted); font-variant: small-caps; letter-spacing: .3px; }
  .main-nav a { position: absolute; color: inherit; text-decoration: none; white-space: nowrap; }

  .hero { position: absolute; left: 297px; top: 42px; }

  .section-title { position: absolute; left: 0; width: 1200px; text-align: center; font-size: 27px; font-weight: 400; }
  .section-rule { position: absolute; height: 2px; background: var(--accent); }

  .about-lead { position: absolute; left: 0; width: 1200px; top: 520px; text-align: center; font-size: 16px; }
  .about-body { position: absolute; left: 488px; width: 306px; top: 563px; text-align: center; font-family: "Tinos", serif; font-size: 9.4px; line-height: 18px; }
  .about-claim { position: absolute; left: 0; width: 1200px; top: 655px; padding-left: 6px; text-align: center; font-family: "Tinos", serif; font-style: italic; font-weight: 700; font-size: 9.5px; }

  .blog-band { position: absolute; left: 297px; top: 717px; }

  .post { position: absolute; top: 895px; width: 143px; height: 189px; background: var(--card); border-radius: 6px; overflow: hidden; }
  .post.faded { opacity: .45; box-shadow: 0 0 6px rgba(0,0,0,.05); }
  .post-image { height: 95px; }
  .post-title { margin: 9px 6px 0; font-size: 10px; font-weight: 700; line-height: 13px; }
  .post-date { margin: 5px 8px 0; font-size: 10px; color: #666; }
  .faded .post-title { color: #777; }
  .faded .post-date { color: #bbb; }

  .site-footer { position: absolute; top: 1171px; font-size: 11px; color: #222; }
</style>
</head>
<body>
  <header class="site-header">
    <div class="brand"><span class="brand-mark"></span><span class="brand-name">Vorlaufwerkstatt</span></div>
    <nav class="main-nav">
      <a style="left:468px">About</a>
      <a style="left:529px">Blog</a>
      <a style="left:585px">Contact</a>
    </nav>
  </header>

  <svg class="hero" width="686" height="345" viewBox="0 0 686 345" role="img" aria-label="Photo of two businessmen in an office looking at a laptop">
    <defs>
      <linearGradient id="heroTone" x1="0" y1="0" x2="1" y2="0.4">
        <stop offset="0" stop-color="#c9d2da"/>
        <stop offset="0.35" stop-color="#8a96a3"/>
        <stop offset="0.7" stop-color="#4c5665"/>
        <stop offset="1" stop-color="#353c48"/>
      </linearGradient>
    </defs>
    <polygon points="0,0 686,0 686,304 509,344 0,294" fill="url(#heroTone)"/>
  </svg>

  <h2 class="section-title" style="top:425px">About</h2>
  <div class="section-rule" style="left:617px; width:47px; top:464px"></div>

  <p class="about-lead">The Vorlaufwerkstatt</p>
  <p class="about-body">is a technology and knowledge transfer company that supports companies in implementing their innovative ideas. We use our large network of scientific institutions.</p>
  <p class="about-claim">Together we will find the right answers for you and your company!</p>

  <svg class="blog-band" width="686" height="440" viewBox="0 0 686 440" aria-hidden="true">
    <polygon points="0,5 194,53 685,0 685,439 0,439" fill="var(--band)"/>
  </svg>

  <h2 class="section-title" style="top:822px">Blog</h2>
  <div class="section-rule" style="left:616px; width:47px; top:860px"></div>

  <article class="post faded" style="left:324px">
    <div class="post-image" role="img" aria-label="Photo of two colleagues working at a laptop" style="background:linear-gradient(120deg,#dfe3e7,#8c95a0)"></div>
    <h3 class="post-title">Innovations in mobile applications</h3>
    <p class="post-date">20/07/2019</p>
  </article>

  <article class="post" style="left:488px">
    <div class="post-image" role="img" aria-label="Abstract blue network over a world map" style="background:radial-gradient(circle at 45% 40%,#5aa8f0,#0d3f9a 55%,#06215c)"></div>
    <h3 class="post-title">Embedded engineering discussions IV</h3>
    <p class="post-date">04/25/2017</p>
  </article>

  <article class="post" style="left:649px">
    <div class="post-image" role="img" aria-label="Photo of a cheering business team" style="background:linear-gradient(180deg,#f4f5f7 0%,#b8c4d4 55%,#3b4356)"></div>
    <h3 class="post-title">Engagement intensified</h3>
    <p class="post-date" style="margin-top:3px">02/14/2018</p>
  </article>

  <article class="post faded" style="left:810px">
    <div class="post-image" role="img" aria-label="Photo of a hand writing on paper" style="background:linear-gradient(120deg,#e9d3c4,#f3efec 60%,#dfe4ec)"></div>
    <h3 class="post-title">Innovation Forum Digitization</h3>
    <p class="post-date">20/07/2019</p>
  </article>

  <footer>
    <p class="site-footer" style="left:330px">© Copyright 2019</p>
    <p class="site-footer" style="left:852px; top:1170px">Terms Of Service</p>
  </footer>
</body>
</html>
```